Waste Oil Filter collection & disposal

Basically I need a 1 page website for the business called Brenmoor Waste Solutions.
We are a environmental service provider and we collect and dispose of waste oil filters to protect the environment from hazardous waste oil products.

This is the link to our current website: www.brenmoorwaste.co.nz

we want it to look fresh and better than our current website. we may potentially look at getting a new logo designed and are open to ideas/designs if you have any.

Industry/Entity Type

Business

Logo Text

Brenmoor Waste Solutions

Number of Pages Required

1 page

Requirements
Must have
• same colours as current website.
• description of what service we provide please refer to leaflet attached

```html
<!DOCTYPE html>
<html lang="en">
<head>
<meta charset="utf-8">
<title>Brenmoor Waste Solutions</title>
<link href="https://fonts.googleapis.com/css2?family=Montserrat:ital,wght@0,400;0,500;0,600;0,700;1,400;1,500&display=swap" rel="stylesheet">
<style>
:root{
  --green:#1e8a3c;
  --green-dark:#16692d;
  --green-band:#1f7a3b;
  --ink:#111;
  --grey:#666;
  --line:#d8d8d8;
  --white:#fff;
}
*{margin:0;padding:0;box-sizing:border-box}
html,body{width:1200px;height:1200px;overflow:hidden;background:var(--white)}
body{font-family:'Montserrat',sans-serif;color:var(--ink);position:relative}
.topbar{position:absolute;left:0;top:0;width:1200px;height:31px;border-bottom:1px solid var(--line);font-size:11px;color:#999}
.topbar .item{position:absolute;top:0;height:30px;display:flex;align-items:center;gap:6px}
.topbar .item b{color:var(--green);font-weight:600}
.topbar .sep{position:absolute;top:0;width:1px;height:30px;background:var(--line)}
.topbar .social{position:absolute;top:0;width:38px;height:30px;border-left:1px solid var(--line);display:flex;align-items:center;justify-content:center}
.topbar .social i{width:9px;height:9px;border-radius:50%;background:#c8c8c8;display:block}
.pickup{position:absolute;left:1037px;top:0;width:137px;height:31px;background:var(--green);color:var(--white);font-size:11.5px;font-weight:700;display:flex;align-items:flex-start;justify-content:center}
.brand{position:absolute;left:55px;top:54px;display:flex;align-items:center;gap:6px}
.brand .mark{width:50px;height:50px;border-radius:50%;background:var(--ink)}
.brand .name{font-size:16px;font-weight:700;line-height:15px;color:var(--green)}
.brand .tag{font-size:6px;color:var(--ink);font-weight:500;margin-top:2px}
.hero{position:absolute;left:0;top:126px;width:1200px;height:540px;overflow:hidden;background:linear-gradient(180deg,#3c5a3a 0%,#9aa39c 30%,#c9cbc8 50%,#2a9a63 70%,#4e5b4c 100%)}
.quote{position:absolute;left:34px;top:261px;width:475px;height:240px;background:rgba(30,138,60,.85);color:var(--white);padding:28px 0 0 46px;font-size:22px;font-weight:600;line-height:28.5px}
.quote .by{margin-top:28px}
.why-rule{position:absolute;left:118px;top:723px;width:2px;height:83px;background:#bbb}
.why-title{position:absolute;left:130px;top:736px;font-size:20px;font-weight:700;line-height:29px;letter-spacing:.1px;white-space:nowrap}
.why-title span{color:var(--green)}
.why-text{position:absolute;left:539px;top:740px;font-size:12.6px;color:var(--grey);line-height:19px}
.band{position:absolute;left:0;top:853px;width:1200px;height:316px;background:radial-gradient(ellipse at 30% 40%,#2f8a48 0%,var(--green-band) 50%,#135a28 100%);color:var(--white)}
.band .icon{position:absolute;left:78px;top:44px;width:78px;height:78px;border-radius:50%;background:rgba(140,220,160,.55)}
.col{position:absolute;top:46px}
.col h2{font-size:21px;font-weight:700;margin-bottom:12px}
.col p{font-size:15.5px;font-weight:600;line-height:19.3px}
.col p+p{margin-top:19px}
.col .cite{font-style:italic;font-weight:400;font-size:15.5px;line-height:17.5px;margin-top:22px}
.process{left:175px}
.oil{left:640px}
</style>
</head>
<body>
<header class="topbar">
  <div class="item" style="left:76px"><svg width="12" height="10" viewBox="0 0 12 10"><rect x=".5" y=".5" width="11" height="9" fill="none" stroke="#bbb"/><path d="M.5 .5 6 5 11.5 .5" fill="none" stroke="#bbb"/></svg>Email: <b>info@brenmoorwaste.co.nz</b></div>
  <div class="sep" style="left:307px"></div>
  <div class="item" style="left:328px"><svg width="10" height="10" viewBox="0 0 10 10"><path d="M2 0 4 3 3 4C4 6 5 7 6 7L7 6 10 8 8 10C4 10 0 6 0 2Z" fill="#bbb"/></svg>Call Us: <b>06 555 0142</b></div>
  <div class="sep" style="left:502px"></div>
  <div class="item" style="left:532px"><svg width="11" height="11" viewBox="0 0 12 12"><circle cx="6" cy="6" r="5" fill="none" stroke="#333" stroke-width="1.3"/><path d="M6 3V6H8" fill="none" stroke="#333"/></svg>Opening Hours: <b>Monday - Friday&nbsp; 7.30am - 5.00pm</b></div>
  <div class="social" style="left:886px"><i></i></div>
  <div class="social" style="left:924px"><i></i></div>
  <div class="social" style="left:962px"><i></i></div>
  <div class="social" style="left:1000px"><i></i></div>
  <div class="pickup">Schedule Pickup</div>
</header>

<div class="brand">
  <div class="mark"></div>
  <div>
    <div class="name">BRENMOOR WASTE<br>SOLUTIONS LTD</div>
    <div class="tag">Our aim is to keep NZ clean</div>
  </div>
</div>

<section class="hero" role="img" aria-label="Photo of a green and white filter collection truck parked on gravel in front of trees">
  <blockquote class="quote">
    "one litre of used oil<br>can contaminate<br>one million litres<br>of water "
    <div class="by">- Harbourview District Council</div>
  </blockquote>
</section>

<section class="why">
  <div class="why-rule"></div>
  <h1 class="why-title">WHY YOU NEED TO CHOOSE<br><span>BRENMOOR WASTE SOLUTIONS LTD</span></h1>
  <p class="why-text">We are passionate about doing our bit in keeping New Zealand Clean and Green.<br>We offer a cost effective system for the collection and disposal of waste oil filters.</p>
</section>

<section class="band" role="img" aria-label="Green tinted photo of crushed oil filters stacked for metal recycling">
  <div class="icon" role="img" aria-label="Recycling symbol"></div>
  <div class="col process">
    <h2>THE PROCESS</h2>
    <p>Filters are collected and transported back<br>to the processing plant.</p>
    <p>At the processing plant they are:<br>Drained<br>Sorted<br>Drained again<br>Crushed into bricks<br>Drained a third time<br>Stacked ready for Metal Recycling</p>
  </div>
  <div class="col oil">
    <h2>WHAT HAPPENS TO THE OIL</h2>
    <p>All residual oil is collected into our<br>tank and then recycled.<br>Currently we are processing over 2,000<br>litres of oil amonth.</p>
    <p class="cite">"recycling engine oil protects the environment and<br>conserves energy resources" - Oil Recycling</p>
    <p class="cite" style="margin-left:4px">"each used oil filterhas on average,more than<br>quarter of a litre of used motor oil" - GreenLoop Recycling</p>
  </div>
</section>
</body>
</html>
```